Website/Logo Design

We need a logo and website design for an opinion mining startup called VantaLume. Our technology mines the web to automatically discover what people are saying about brands, products, etc. The project we are fielding here is for our informational, public-facing website. In its initial incarnation, it will simply be a vehicle for marketing materials and information on our company and its offerings, but it should be flexible enough to expand as more content/functionality is added.

Some designs we like are:
http://www.tradewhisk.example
http://www.gorvantel.example
http://www.kfz.example
http://www.lintwharf.example
http://moxbarrel.example
http://trundlemq.example
http://www.zopla.example
Updates

All, please try to shy away from using a photo of a person as the focal point of the design.  Our company is more technological than social.

Target Market(s)

Primarily businesses interested in sentiment analysis (typically companies involved in advertising, market research, PR, etc.)

Industry/Entity Type

It Company

Requirements
Must have
• We are looking for a clean, modern, and professional design. This includes a logo, homepage, and internal page if it will differ from the homepage.
Nice to have
• It would be excellent if you could provide an HTML mockup if your design is chosen.
Should not have
• Flash, excessive bells and whistles

```html
<!DOCTYPE html>
<html lang="en">
<head>
<meta charset="utf-8">
<title>VantaLume — Who we are</title>
<link rel="stylesheet" href="https://fonts.googleapis.com/css2?family=Bebas+Neue&family=Arimo:wght@400;700&family=Open+Sans:wght@400;600&display=swap">
<style>
  :root {
    --ink: #000000;
    --red: #ee1c25;
    --panel: #f5f5f5;
    --paper: #ffffff;
    --rule-grey: #9a9a9a;
    --text: #111111;
  }
  * { margin: 0; padding: 0; box-sizing: border-box; }
  html, body { width: 1200px; height: 1200px; overflow: hidden; background: var(--paper); }
  body { position: relative; font-family: "Arimo", Arial, sans-serif; color: var(--text); }

  .top-bar { position: absolute; top: 0; left: 0; width: 1200px; height: 12px; background: var(--ink); }

  .site-header { position: absolute; top: 12px; left: 120px; width: 960px; height: 168px; background: var(--panel); }
  .brand { position: absolute; left: 48px; top: 112px; display: flex; align-items: center; gap: 7px; white-space: nowrap;
    font-family: "Bebas Neue", sans-serif; font-size: 24px; letter-spacing: 1px; color: var(--ink); line-height: 1; }
  .brand-square { width: 12px; height: 12px; background: var(--red); }

  .tagline { position: absolute; left: 228px; top: 16px; width: 715px; height: 74px; background: var(--paper);
    padding: 18px 20px 0 20px; font-size: 16px; letter-spacing: 1.6px; line-height: 19px; color: var(--ink); }
  .tagline::before { content: ""; position: absolute; left: -32px; top: 44px;
    border-style: solid; border-width: 0 32px 14px 0; border-color: transparent var(--paper) transparent transparent; }

  .main-nav { position: absolute; left: 224px; top: 114px; width: 720px; display: flex; justify-content: space-between;
    align-items: center; white-space: nowrap;
    font-family: "Bebas Neue", sans-serif; font-size: 29px; letter-spacing: 2px; line-height: 1; }
  .main-nav a { color: var(--ink); text-decoration: none; padding: 1px 6px 0; white-space: nowrap; }
  .main-nav a.is-active { background: var(--red); color: var(--paper); }
  .main-nav .sep { font-family: "Arimo", sans-serif; font-size: 12px; margin-top: 8px; color: var(--ink); }

  .header-rule { position: absolute; top: 180px; left: 120px; width: 960px; height: 10px; background: var(--ink); }

  .content-panel { position: absolute; top: 204px; left: 120px; width: 960px; height: 480px; background: var(--panel);
    border-bottom: 3px solid var(--ink); padding: 20px 38px 0 35px; }
  .corner { position: absolute; top: 0; width: 0; height: 0; border-style: solid; }
  .corner-left { left: 0; border-width: 22px 22px 0 0; border-color: var(--ink) transparent transparent transparent; }
  .corner-right { right: 0; border-width: 0 22px 22px 0; border-color: transparent var(--ink) transparent transparent; }
  .page-title { font-size: 34px; font-weight: 400; margin: 4px 0 14px 3px; letter-spacing: -0.3px; color: var(--ink); }
  .team-photo { float: left; width: 367px; height: 224px; margin: 2px 12px 0 0;
    background: linear-gradient(100deg, #d9d2c8 0%, #c7b8a4 30%, #9fa7b4 60%, #e8e8ec 100%); }
  .intro-text { font-size: 18.5px; line-height: 23px; color: var(--ink); hyphens: auto; }
  .intro-text p:first-of-type { text-indent: 43px; }

  .footer-nav { position: absolute; top: 714px; left: 0; width: 1200px; display: flex; justify-content: center; align-items: center;
    font-family: "Open Sans", sans-serif; font-size: 13px; color: var(--ink); white-space: nowrap; }
  .footer-nav a { color: var(--ink); text-decoration: none; border-bottom: 1px solid var(--ink); line-height: 15px; }
  .footer-nav a.is-active { background: var(--ink); color: var(--paper); padding: 1px 6px; border: 0; }
  .footer-nav .sep { margin: 0 14px; }
  .legal { position: absolute; top: 751px; left: 0; width: 1200px; display: flex; justify-content: center; align-items: center;
    font-family: "Open Sans", sans-serif; font-size: 12.5px; color: var(--ink); white-space: nowrap; }
  .legal .copyright { margin: 0 32px 0 -12px; }
  .legal a { color: var(--ink); text-decoration: none; border-bottom: 1px solid var(--ink); line-height: 15px; }
  .legal .sep { margin: 0 14px; }

  .cut-line { position: absolute; top: 798px; left: 0; width: 1200px; border-top: 2px dashed var(--rule-grey); }

  .concepts-title { position: absolute; top: 829px; left: 38px; font-family: "Bebas Neue", sans-serif; font-size: 18px;
    letter-spacing: 1.5px; color: var(--ink); white-space: nowrap; }
  .concept { position: absolute; top: 1010px; width: 200px; margin-left: -100px; text-align: center; }
  .concept-name { display: inline-flex; align-items: center; gap: 6px; font-family: "Bebas Neue", sans-serif;
    font-size: 22px; letter-spacing: 1px; color: var(--ink); line-height: 1; white-space: nowrap; }
  .concept-mark { width: 10px; height: 10px; background: var(--red); }
  .concept-number { margin-top: 28px; font-size: 19px; color: var(--ink); }
</style>
</head>
<body>
  <div class="top-bar"></div>

  <header class="site-header">
    <div class="brand"><span class="brand-square"></span>VantaLume</div>
    <div class="tagline">Our technology mines the web to automatically discover what people are saying about brands, products, etc...</div>
    <nav class="main-nav">
      <a class="is-active" href="#">Who we are</a><span class="sep">/</span>
      <a href="#">What we do</a><span class="sep">/</span>
      <a href="#">Our client</a><span class="sep">/</span>
      <a href="#">Price</a><span class="sep">/</span>
      <a href="#">Contact us</a>
    </nav>
  </header>
  <div class="header-rule"></div>

  <main class="content-panel">
    <span class="corner corner-left"></span>
    <span class="corner corner-right"></span>
    <h1 class="page-title">who we are?</h1>
    <div class="intro-text">
      <div class="team-photo" role="img" aria-label="Photo of a smiling team of five business people in office attire"></div>
      <p>International is a worldwide movement of people who campaign for internationally recognized human rights for all.Our supporters are outraged by human rights abuses but inspired by hope for a better world - so we work to improve human rights through campaigning and international solidarity. We have more than 2.8 million members and supporters in more than 150 countries and regions and we coordinate this support to act for justice on a wide range of issues. You can help make a real difference by becoming a member or sup&shy;porter of Halvren Collective ...</p>
      <p>International is a worldwide movement of people who campaign for internationally recognized human rights for all.Our supporters are outraged by human rights abuses but inspired by hope for a better world - so we work to improve human rights through campaigning and international solidarity. We have more than 2.8 mil&shy;lion members and supporters in more than 150 countries and regions and we coordinate this support to act for justice on a wide range of issues. You can help make a real difference by becoming a member or sup&shy;porter of Halvren Collective ...</p>
    </div>
  </main>

  <nav class="footer-nav">
    <a class="is-active" href="#">Who we are</a><span class="sep">|</span>
    <a href="#">What we do</a><span class="sep">|</span>
    <a href="#">Our client</a><span class="sep">|</span>
    <a href="#">Price</a><span class="sep">|</span>
    <a href="#">Contact us</a>
  </nav>
  <div class="legal">
    <span class="copyright">Copyright © 2010 VantaLume Inc. All rights reserved.</span>
    <a href="#">Terms of Use</a><span class="sep">|</span><a href="#">Privacy Policy</a>
  </div>

  <div class="cut-line"></div>

  <h2 class="concepts-title">Logo concepts</h2>
  <div class="concept" style="left:240px"><div class="concept-name"><span class="concept-mark"></span>VantaLume</div><div class="concept-number">1.</div></div>
  <div class="concept" style="left:480px"><div class="concept-name"><span class="concept-mark"></span>VantaLume</div><div class="concept-number">2.</div></div>
  <div class="concept" style="left:728px"><div class="concept-name"><span class="concept-mark"></span>VantaLume</div><div class="concept-number">3.</div></div>
  <div class="concept" style="left:978px"><div class="concept-name"><span class="concept-mark"></span>VantaLume</div><div class="concept-number">4.</div></div>
</body>
</html>
```